Tallmere Learning Graphic Design Project

I need graphic design elements to establish a look and feel for my company, Tallmere Learning. I work with companies and organizations who are either starting out in eLearning and need direction or have been at it for a while and could do it better. I work inside the organization to analyse their current learning, devise strategic plans and then stay around to help implement them. This saves the organization a lot of money and gives them happier and more able workers.
I have been working in this industry for many years and see the need for a very specific consultancy focused on the strategies behind adult learning offerings that involve screens (this is almost all).
Tallmere thinks outside the box. But it also follows up with concrete results. Surprising things can be achieved. This is the kind of feeling I'd like to convey in the Tallmere look and feel. So I'm looking for a set of graphic elements that can be used mainly for business cards and website objects. To give you an idea of the style of thing I like I have attached a business card template that I like. What I like is its freshness and clarity. But open to all ideas. Thanks and good luck.
Updates

 I've posted a new image  to show what I mean by clean and fresh. Not suggesting that I need a cord with a knot in it but I really like the colour, contrast and sort of starkness of the image. Suggesting this as apossible direction change to use with those good ideas already submitted and to help clarify for new ones. Thanks again.

                                   

Target Market(s)

corporates and larger organizations - any organization that has or wants to have elearning in their training mix.

Industry/Entity Type

Graphic Design

Requirements
Must have
• elements that can be used to create a website, business cards, other materials as required. So this might include a font recommendation and a number of illustrations that can be used together or separately.
Nice to have
• nice if you could include the elements designed as a business card in a ready-to-print format.
Should not have
• don't really want a logo in the usual sense

```html
<!DOCTYPE html>
<html lang="en">
<head>
<meta charset="utf-8">
<title>Tallmere Learning – Business Card</title>
<link rel="stylesheet" href="https://fonts.googleapis.com/css2?family=Arimo:wght@400;700&family=Pinyon+Script&display=swap">
<style>
  :root {
    --sky-deep: #1f7fd6;
    --sky-mid: #4aaee8;
    --sky-light: #bfe6fa;
    --meadow-green: #7fbf4a;
    --meadow-pale: #cfe7a8;
    --band-blue: #1a92ea;
    --text-white: #ffffff;
    --text-dark: #111111;
    --page-bg: #ffffff;
  }
  * { margin: 0; padding: 0; box-sizing: border-box; }
  html, body {
    width: 1200px;
    height: 789px;
    overflow: hidden;
    background: var(--page-bg);
  }
  .card {
    position: relative;
    width: 1200px;
    height: 789px;
    overflow: hidden;
    font-family: "Arimo", Arial, sans-serif;
  }
  .card__scene {
    position: absolute;
    inset: 0;
    background:
      radial-gradient(circle at 88% 14%, rgba(255,255,255,0.9) 0, rgba(255,255,255,0) 22%),
      linear-gradient(180deg, rgba(0,0,0,0) 40%, rgba(207,231,168,0.55) 62%, var(--meadow-green) 100%),
      linear-gradient(110deg, var(--sky-deep) 0%, var(--sky-mid) 55%, var(--sky-light) 100%);
  }
  .card__name {
    position: absolute;
    left: 160px;
    top: 68px;
    font-size: 60px;
    font-weight: 400;
    color: var(--text-white);
    letter-spacing: 0.5px;
  }
  .card__role {
    position: absolute;
    left: 215px;
    top: 148px;
    font-size: 41px;
    color: var(--text-dark);
  }
  .card__contact {
    position: absolute;
    left: 217px;
    top: 254px;
    list-style: none;
    font-size: 41px;
    line-height: 51px;
    color: var(--text-dark);
  }
  .card__tagline {
    position: absolute;
    left: 118px;
    top: 540px;
    font-size: 38px;
    font-weight: 700;
    color: var(--text-dark);
    letter-spacing: 0.3px;
  }
  .card__band {
    position: absolute;
    left: 0;
    top: 600px;
    width: 1200px;
    height: 158px;
    background: var(--band-blue);
    border-top: 3px solid var(--text-white);
  }
  .card__brand {
    position: absolute;
    left: 0;
    right: 0;
    top: 8px;
    text-align: center;
    font-family: "Pinyon Script", cursive;
    font-size: 100px;
    line-height: 130px;
    color: var(--text-white);
  }
  .card__grass {
    position: absolute;
    left: 0;
    top: 758px;
    width: 1200px;
    height: 31px;
    background: linear-gradient(180deg, var(--meadow-pale), var(--meadow-green));
  }
</style>
</head>
<body>
  <main class="card">
    <div class="card__scene" role="img" aria-label="Bright blue sky with sunlight, a meadow of wildflowers and grasses, and fluttering butterflies"></div>

    <h1 class="card__name">Maren Holloway</h1>
    <p class="card__role">eLearning strategist</p>
    <ul class="card__contact">
      <li>0491 570 156</li>
      <li>maren@tallmere.net.au</li>
      <li>www.tallmere.net.au</li>
    </ul>

    <p class="card__tagline">never stop creating / never stop learning</p>

    <div class="card__band">
      <p class="card__brand">Tallmere Learning</p>
    </div>
    <div class="card__grass" role="img" aria-label="Strip of meadow grass and flowers"></div>
  </main>
</body>
</html>
```